standardize print collateral

we need help standardizing all print collateral and website. top priorities:

1. standardized case studies template
2. standardized marketing slicks template
3. standardized powerpoint template
Updates

Project Deadline Extended
Reason: We are extending the project to allow current design submissions to be tweaked while providing the opportunity for new designs to be submitted. We will need all 3 collateral designs submitted to make a final decision. Please note, these 3 designs should all look different, needless to say they should all compliment eachother. As for some direction, the powerpoint main color should not be yellow since yellow does not show up the same shade on any screen. The case study and marketing slicks will be printed and often sit next to our competitors marketing material - think high end product, technology, revolutionary, edgy, professional. The designs should compliment eachother and feel like the Brightfen Metrics brand (which you are determining) and should stand out professionally. We are open to introducing new colors into our brand, the only thing that must remain the same is our logo. Have fun, make it edgy, and keep it professional. Looking forward to seeing what you submit!

Target Market(s)

Property Casualty Insurance Companies: Executive level wording with actuarial credibility

Industry/Entity Type

Marketing

Requirements
Must have
• professional layout for existing collateral and 2-page marketing slicks. style guide/colors can be transferred to powerpoint. logo must stay; everything else (i.e. color, font, layout/structure etc.) is flexible. The three components should not looks the same, they should only compliment eachother.
Nice to have
• we are revolutionizing a conservative industry, so adequate level of edgy/advanced technology/impactful feel to layout
Should not have
• no need to stay within color constraints of yellow, but need to appropriately work well with the eagle head logo

```html
<!DOCTYPE html>
<html lang="en">
<head>
<meta charset="utf-8">
<title>Rapid Portfolio Analysis – Brightfen Metrics</title>
<link rel="stylesheet" href="https://fonts.googleapis.com/css2?family=Carlito:wght@400;700&family=Arimo:wght@400&display=swap">
<style>
  :root {
    --black: #0d0d0d;
    --yellow: #f2b418;
    --grey-swoosh: #a7a7a7;
    --panel: #a3a3a3;
    --ink: #2b2b2b;
    --muted: #7a7a7a;
    --white: #ffffff;
    --cell-green: #8fd18a;
    --cell-lime: #c6e67a;
    --cell-yellow: #f7e36a;
    --cell-orange: #f5a653;
    --cell-red: #ec6a5e;
    --bar-green: #2f9e3a;
    --bar-yellow: #f1c232;
    --bar-red: #d63c2f;
    --grid: #d5d5d5;
  }
  * { box-sizing: border-box; margin: 0; padding: 0; }
  html, body { width: 847px; height: 1200px; overflow: hidden; background: var(--white); }
  body { font-family: "Carlito", "Calibri", sans-serif; color: var(--ink); }
  .page { position: relative; width: 847px; height: 1200px; overflow: hidden; }

  .masthead { position: absolute; inset: 0 0 auto 0; height: 185px; }
  .masthead svg { position: absolute; inset: 0; }
  .title {
    position: absolute; left: 60px; top: 28px;
    font-weight: 700; font-size: 40px; line-height: 41px; color: var(--white);
  }
  .subtitle {
    position: absolute; left: 60px; top: 118px;
    font-family: "Arimo", Arial, sans-serif; font-size: 21px; color: var(--white);
  }
  .brand {
    position: absolute; left: 650px; top: 80px;
    display: flex; align-items: center; gap: 7px;
    font-weight: 700; font-size: 19px; color: #555;
  }
  .brand-dot { width: 14px; height: 14px; border-radius: 50%; background: var(--yellow); }

  .intro {
    position: absolute; left: 62px; top: 234px; width: 735px;
    font-size: 15px; line-height: 19px; color: #333;
  }

  .how-panel {
    position: absolute; left: 62px; top: 360px; width: 373px; height: 670px;
    background: var(--panel); color: var(--white); padding: 38px 20px 0 22px;
  }
  .how-title { font-size: 36px; font-weight: 400; margin-bottom: 34px; }
  .step { margin-bottom: 44px; }
  .step-head { font-size: 15.5px; margin-bottom: 4px; }
  .step-name { font-size: 20px; }
  .step-body { font-size: 15.5px; line-height: 22.5px; }

  .figure { position: absolute; left: 474px; width: 324px; }
  .figure-title { text-align: center; font-weight: 700; font-size: 16px; color: #222; margin-bottom: 6px; }
  .figure-caption { font-size: 13.5px; line-height: 16px; color: #333; margin-top: 8px; }

  .portfolio-table { width: 100%; border-collapse: collapse; font-size: 5.6px; line-height: 7px; color: #222; }
  .portfolio-table th { font-weight: 700; text-align: center; padding: 1px; border-bottom: 1px solid #555; vertical-align: bottom; }
  .portfolio-table td { text-align: right; padding: 1px 2px; border-bottom: 1px solid #e6e6e6; white-space: nowrap; }
  .portfolio-table td:first-child { text-align: left; }
  .portfolio-table .total td { border-top: 1px solid #555; font-weight: 700; }
  .portfolio-table .avg td { border: none; }
  .rl-yellow { background: var(--cell-yellow); }
  .rl-orange { background: var(--cell-orange); }
  .rl-green { background: var(--cell-green); }
  .sc-lime { background: var(--cell-lime); }
  .sc-red { background: var(--cell-red); }

  .dashboard { width: 324px; height: 280px; border: 1px solid #999; background: #f4f4f4; overflow: hidden; }
  .dash-bar { height: 8px; background: linear-gradient(#cfd9e8, #a9b9d2); display: flex; justify-content: flex-end; gap: 2px; padding: 1px 3px; }
  .dash-bar span { width: 6px; height: 5px; background: #d44; }
  .dash-tools { height: 10px; background: #e8e8e8; border-bottom: 1px solid #bbb; }
  .dash-strip { display: flex; height: 44px; gap: 2px; padding: 3px 3px 3px 28px; background: #fff; border-bottom: 1px solid #bbb; }
  .dash-strip div { flex: 1; background: linear-gradient(#3d9a45, #bfe3b8); }
  .dash-strip .red { flex: .25; background: linear-gradient(#d33, #f6b0a6); }
  .dash-strip .blue { flex: .8; background: linear-gradient(#6f8bb2, #eef2f7); }
  .dash-head, .dash-row {
    display: grid; grid-template-columns: 20px 24px 24px 66px 42px 24px 48px 1fr;
    font-size: 3.6px; align-items: center; gap: 2px; padding: 0 2px;
  }
  .dash-head { height: 10px; font-weight: 700; background: #fff; border-bottom: 1px solid #999; }
  .dash-row { height: 8.3px; background: #fff; border-bottom: 1px solid #eee; }
  .dash-row:nth-child(odd) { background: #fafafa; }
  .stack { display: flex; height: 5px; }
  .stack .g { background: var(--bar-green); }
  .stack .y { background: var(--bar-yellow); }
  .stack .r { background: var(--bar-red); }
  .mini { height: 4px; background: var(--bar-red); }
  .mini.g { background: var(--bar-green); }

  .report-title {
    position: absolute; left: 62px; top: 1036px;
    font-weight: 700; font-size: 27.5px; color: #151515;
  }
  .report-body {
    position: absolute; left: 62px; top: 1076px; width: 735px;
    font-size: 14px; line-height: 17.5px; color: var(--muted);
  }
</style>
</head>
<body>
<div class="page">

  <header class="masthead">
    <svg width="847" height="185" viewBox="0 0 847 185" aria-hidden="true">
      <path d="M0 0 H655 C620 70 575 125 505 150 C430 176 330 180 0 180 Z" fill="var(--black)"/>
      <path d="M505 150 C560 128 600 90 630 40 C620 110 585 160 530 182 L380 182 C440 176 475 165 505 150 Z" fill="var(--yellow)"/>
      <path d="M847 140 C760 150 660 168 560 182 L847 182 Z" fill="var(--grey-swoosh)"/>
    </svg>
    <h1 class="title">Rapid Portfolio<br>Analysis</h1>
    <p class="subtitle">Winning Against Adverse Selection</p>
    <div class="brand"><span class="brand-dot"></span>Brightfen Metrics</div>
  </header>

  <p class="intro">The property and casualty market is over-supplied with excess capacity, and current pricing methods are inconsistent and outdated. This leads to a considerable level of adverse selection within nearly every portfolio. Almost every insurer is attracting customers who are underpriced and losing business where they are overpriced. This invisible effect only surfaces after evidence of slowly deteriorating portfolio loss ratios, resulting in premium increases across the portfolio. These across-the-board premium increases exacerbate the problem by overpricing the most profitable customers and driving them into the arms of competitors.</p>

  <section class="how-panel">
    <h2 class="how-title">How does it work?</h2>
    <div class="step">
      <p class="step-head"><span class="step-name">Detection</span> : Is the portfolio priced correctly?</p>
      <p class="step-body">Vantix employs a regression method based on a technological breakthrough. It exposes pricing imbalances by commonly employed rating methods including the GLM. These pricing imbalances are the major drivers of adverse selection.</p>
    </div>
    <div class="step">
      <p class="step-head"><span class="step-name">Measurement</span> : How is the portfolio trending?</p>
      <p class="step-body">Vantix scores the two most important attributes of the portfolio: the adequacy of rates and the quality of the business on a progressive basis. In addition, Vantix projects the financial outcome of business as it is written with startling accuracy. Insurers are able to know significantly in advance of trends in their business.</p>
    </div>
    <div class="step">
      <p class="step-head"><span class="step-name">Correction</span> : How to address the issues?</p>
      <p class="step-body">Vantix provides an array of options for addressing any deterioration in the portfolio. These options range from specifically designed rate adjustments and underwriting strategies, to simple distribution management sales and profitability strategies.</p>
    </div>
  </section>

  <figure class="figure" style="top:360px">
    <h3 class="figure-title">Portfolio Monitoring</h3>
    <table class="portfolio-table">
      <thead>
        <tr><th>Policy Effective Period</th><th>Earned Exposure</th><th>Earned Premiums</th><th>Losses</th><th>Claims</th><th>Loss Ratios</th><th>Rate Level</th><th>Port-folio Score</th><th>Good Percent Exposure</th><th>Average Percent Exposure</th><th>Poor Percent Exposure</th></tr>
      </thead>
      <tbody>
        <tr><td>2001/Q1</td><td>35,900</td><td>$11,918,029</td><td>$9,340,199</td><td>462</td><td>78.37%</td><td class="rl-yellow">0.968</td><td class="sc-lime">523</td><td>35.51%</td><td>41.86%</td><td>22.62%</td></tr>
        <tr><td>2001/Q2</td><td>43,828</td><td>$14,423,434</td><td>$6,216,889</td><td>570</td><td>43.10%</td><td class="rl-orange">0.959</td><td class="sc-lime">532</td><td>38.99%</td><td>40.11%</td><td>20.90%</td></tr>
        <tr><td>2001/Q3</td><td>43,883</td><td>$14,317,681</td><td>$9,396,107</td><td>486</td><td>65.63%</td><td class="rl-orange">0.962</td><td class="sc-lime">530</td><td>38.70%</td><td>39.17%</td><td>22.13%</td></tr>
        <tr><td>2001/Q4</td><td>37,145</td><td>$13,590,766</td><td>$8,257,472</td><td>408</td><td>60.76%</td><td class="rl-yellow">0.97</td><td class="sc-lime">524</td><td>36.83%</td><td>40.75%</td><td>22.42%</td></tr>
        <tr><td>2007/Q1</td><td>37,989</td><td>$21,200,710</td><td>$9,342,857</td><td>359</td><td>44.07%</td><td class="rl-green">1.048</td><td class="sc-red">495</td><td>31.81%</td><td>35.59%</td><td>32.60%</td></tr>
        <tr><td>2007/Q2</td><td>47,247</td><td>$23,940,671</td><td>$7,413,443</td><td>490</td><td>30.97%</td><td class="rl-green">1.042</td><td class="rl-orange">502</td><td>33.42%</td><td>36.68%</td><td>29.90%</td></tr>
        <tr><td>2007/Q3</td><td>40,984</td><td>$20,473,565</td><td>$8,208,414</td><td>383</td><td>40.09%</td><td class="rl-green">1.033</td><td class="rl-orange">501</td><td>33.48%</td><td>35.73%</td><td>30.79%</td></tr>
        <tr><td>2007/Q4</td><td>36,524</td><td>$23,560,720</td><td>$10,684,146</td><td>491</td><td>45.35%</td><td class="rl-green">1.076</td><td class="sc-red">492</td><td>31.52%</td><td>34.81%</td><td>33.67%</td></tr>
        <tr><td>2008/Q1</td><td>40,671</td><td>$21,959,902</td><td>$7,190,574</td><td>371</td><td>32.74%</td><td class="rl-green">1.073</td><td class="sc-red">493</td><td>31.15%</td><td>34.21%</td><td>34.64%</td></tr>
        <tr><td>2008/Q2</td><td>47,291</td><td>$24,645,178</td><td>$9,865,707</td><td>424</td><td>40.03%</td><td class="rl-green">1.055</td><td class="rl-orange">501</td><td>33.11%</td><td>35.80%</td><td>31.09%</td></tr>
        <tr><td>2008/Q3</td><td>38,289</td><td>$18,831,701</td><td>$4,134,801</td><td>321</td><td>21.96%</td><td class="rl-green">1.058</td><td class="sc-red">497</td><td>32.65%</td><td>34.69%</td><td>32.66%</td></tr>
        <tr><td>2008/Q4</td><td>32,858</td><td>$17,184,279</td><td>$4,128,538</td><td>264</td><td>24.03%</td><td class="rl-green">1.075</td><td class="sc-red">489</td><td>30.50%</td><td>34.30%</td><td>35.21%</td></tr>
        <tr class="total"><td>Total</td><td>1,211,762</td><td>$595,065,402</td><td>$232,385,615</td><td>12,986</td><td>39.05%</td><td>1</td><td>520</td><td>36.93%</td><td>38.76%</td><td>24.31%</td></tr>
        <tr class="avg"><td colspan="8">Average Loss Ratio</td><td>26%</td><td>40%</td><td>53%</td></tr>
      </tbody>
    </table>
    <figcaption class="figure-caption">Predict the future loss ratio of the business being written - both renewals and new business</figcaption>
  </figure>

  <figure class="figure" style="top:670px">
    <h3 class="figure-title">Distribution Monitoring</h3>
    <div class="dashboard">
      <div class="dash-bar"><span></span></div>
      <div class="dash-tools"></div>
      <div class="dash-strip"><div></div><div></div><div class="blue"></div><div class="red"></div><div class="red"></div><div></div></div>
      <div class="dash-head"><span>Agent</span><span>WP Change</span><span>NB Change</span><span>Current Premium Mix</span><span>Selection Rate</span><span>Exposure</span><span>Top Shift Change</span><span>Diff (chg)</span></div>
      <div class="dash-row"><span>07010</span><span>-16 %</span><span>-25 %</span><div class="stack"><i class="g" style="width:40%"></i><i class="y" style="width:25%"></i><i class="r" style="width:35%"></i></div><span>60 %</span><span>154,923</span><span>— —</span><div class="mini" style="width:40%"></div></div>
      <div class="dash-row"><span>07019</span><span>0 %</span><span>-21 %</span><div class="stack"><i class="g" style="width:55%"></i><i class="y" style="width:15%"></i><i class="r" style="width:30%"></i></div><span>76 %</span><span>8,134</span><span>— —</span><div class="mini g" style="width:30%"></div></div>
      <div class="dash-row"><span>07122</span><span>-35 %</span><span>-39 %</span><div class="stack"><i class="g" style="width:30%"></i><i class="y" style="width:20%"></i><i class="r" style="width:50%"></i></div><span>64 %</span><span>4,581</span><span>— —</span><div class="mini" style="width:55%"></div></div>
      <div class="dash-row"><span>07262</span><span>-1 %</span><span>-15 %</span><div class="stack"><i class="g" style="width:62%"></i><i class="y" style="width:18%"></i><i class="r" style="width:20%"></i></div><span>64 %</span><span>6,408</span><span>— —</span><div class="mini g" style="width:25%"></div></div>
      <div class="dash-row"><span>09641</span><span>-12 %</span><span>-28 %</span><div class="stack"><i class="g" style="width:45%"></i><i class="y" style="width:10%"></i><i class="r" style="width:45%"></i></div><span>72 %</span><span>4,287</span><span>— —</span><div class="mini" style="width:35%"></div></div>
      <div class="dash-row"><span>07025</span><span>-39 %</span><span>-21 %</span><div class="stack"><i class="g" style="width:35%"></i><i class="y" style="width:25%"></i><i class="r" style="width:40%"></i></div><span>72 %</span><span>6,018</span><span>— —</span><div class="mini" style="width:45%"></div></div>
      <div class="dash-row"><span>09508</span><span>17 %</span><span>4 %</span><div class="stack"><i class="g" style="width:70%"></i><i class="y" style="width:12%"></i><i class="r" style="width:18%"></i></div><span>72 %</span><span>5,416</span><span>— —</span><div class="mini g" style="width:50%"></div></div>
      <div class="dash-row"><span>07192</span><span>10 %</span><span>-16 %</span><div class="stack"><i class="g" style="width:50%"></i><i class="y" style="width:20%"></i><i class="r" style="width:30%"></i></div><span>71 %</span><span>5,172</span><span>— —</span><div class="mini g" style="width:20%"></div></div>
      <div class="dash-row"><span>06693</span><span>-33 %</span><span>-15 %</span><div class="stack"><i class="g" style="width:38%"></i><i class="y" style="width:22%"></i><i class="r" style="width:40%"></i></div><span>57 %</span><span>4,003</span><span>— —</span><div class="mini" style="width:30%"></div></div>
      <div class="dash-row"><span>03444</span><span>-1 %</span><span>-27 %</span><div class="stack"><i class="g" style="width:58%"></i><i class="y" style="width:14%"></i><i class="r" style="width:28%"></i></div><span>36 %</span><span>3,727</span><span>— —</span><div class="mini g" style="width:28%"></div></div>
      <div class="dash-row"><span>09677</span><span>-18 %</span><span>4 %</span><div class="stack"><i class="g" style="width:48%"></i><i class="y" style="width:16%"></i><i class="r" style="width:36%"></i></div><span>72 %</span><span>3,601</span><span>— —</span><div class="mini" style="width:38%"></div></div>
      <div class="dash-row"><span>03448</span><span>-18 %</span><span>-28 %</span><div class="stack"><i class="g" style="width:42%"></i><i class="y" style="width:18%"></i><i class="r" style="width:40%"></i></div><span>42 %</span><span>3,127</span><span>— —</span><div class="mini" style="width:42%"></div></div>
      <div class="dash-row"><span>07030</span><span>-23 %</span><span>-12 %</span><div class="stack"><i class="g" style="width:52%"></i><i class="y" style="width:18%"></i><i class="r" style="width:30%"></i></div><span>60 %</span><span>2,829</span><span>— —</span><div class="mini g" style="width:36%"></div></div>
      <div class="dash-row"><span>03202</span><span>-12 %</span><span>-25 %</span><div class="stack"><i class="g" style="width:36%"></i><i class="y" style="width:24%"></i><i class="r" style="width:40%"></i></div><span>37 %</span><span>2,751</span><span>— —</span><div class="mini" style="width:32%"></div></div>
      <div class="dash-row"><span>09748</span><span>15 %</span><span>77 %</span><div class="stack"><i class="g" style="width:66%"></i><i class="y" style="width:14%"></i><i class="r" style="width:20%"></i></div><span>82 %</span><span>2,493</span><span>— —</span><div class="mini g" style="width:44%"></div></div>
      <div class="dash-row"><span>08282</span><span>7 %</span><span>-56 %</span><div class="stack"><i class="g" style="width:40%"></i><i class="y" style="width:20%"></i><i class="r" style="width:40%"></i></div><span>73 %</span><span>2,402</span><span>— —</span><div class="mini" style="width:26%"></div></div>
      <div class="dash-row"><span>07282</span><span>-1 %</span><span>1 %</span><div class="stack"><i class="g" style="width:60%"></i><i class="y" style="width:15%"></i><i class="r" style="width:25%"></i></div><span>62 %</span><span>2,050</span><span>— —</span><div class="mini g" style="width:32%"></div></div>
      <div class="dash-row"><span>03458</span><span>-16 %</span><span>-39 %</span><div class="stack"><i class="g" style="width:34%"></i><i class="y" style="width:20%"></i><i class="r" style="width:46%"></i></div><span>33 %</span><span>1,869</span><span>— —</span><div class="mini" style="width:48%"></div></div>
      <div class="dash-row"><span>07046</span><span>-17 %</span><span>-22 %</span><div class="stack"><i class="g" style="width:50%"></i><i class="y" style="width:18%"></i><i class="r" style="width:32%"></i></div><span>70 %</span><span>1,815</span><span>— —</span><div class="mini" style="width:30%"></div></div>
      <div class="dash-row"><span>07294</span><span>-28 %</span><span>-41 %</span><div class="stack"><i class="g" style="width:30%"></i><i class="y" style="width:22%"></i><i class="r" style="width:48%"></i></div><span>73 %</span><span>1,816</span><span>— —</span><div class="mini" style="width:40%"></div></div>
      <div class="dash-row"><span>04605</span><span>-22 %</span><span>-41 %</span><div class="stack"><i class="g" style="width:44%"></i><i class="y" style="width:16%"></i><i class="r" style="width:40%"></i></div><span>42 %</span><span>1,678</span><span>— —</span><div class="mini" style="width:34%"></div></div>
      <div class="dash-row"><span>07180</span><span>4 %</span><span>33 %</span><div class="stack"><i class="g" style="width:64%"></i><i class="y" style="width:14%"></i><i class="r" style="width:22%"></i></div><span>73 %</span><span>1,673</span><span>— —</span><div class="mini g" style="width:38%"></div></div>
      <div class="dash-row"><span>04406</span><span>-37 %</span><span>-60 %</span><div class="stack"><i class="g" style="width:28%"></i><i class="y" style="width:24%"></i><i class="r" style="width:48%"></i></div><span>36 %</span><span>1,719</span><span>— —</span><div class="mini" style="width:50%"></div></div>
      <div class="dash-row"><span>07551</span><span>-14 %</span><span>-9 %</span><div class="stack"><i class="g" style="width:54%"></i><i class="y" style="width:16%"></i><i class="r" style="width:30%"></i></div><span>69 %</span><span>1,559</span><span>— —</span><div class="mini g" style="width:26%"></div></div>
      <div class="dash-row"><span>09638</span><span>9 %</span><span>-18 %</span><div class="stack"><i class="g" style="width:46%"></i><i class="y" style="width:18%"></i><i class="r" style="width:36%"></i></div><span>45 %</span><span>1,494</span><span>— —</span><div class="mini" style="width:30%"></div></div>
      <div class="dash-row"><span>07551</span><span>-20 %</span><span>13 %</span><div class="stack"><i class="g" style="width:58%"></i><i class="y" style="width:14%"></i><i class="r" style="width:28%"></i></div><span>69 %</span><span>1,473</span><span>— —</span><div class="mini g" style="width:22%"></div></div>
    </div>
    <figcaption class="figure-caption">Constantly track the quality and performance of individual distribution outlets based on the underwriting score of each policy</figcaption>
  </figure>

  <h2 class="report-title">Let Brightfen Metrics Build Your Portfolio Analysis Report</h2>
  <p class="report-body">The report details your portfolio trends and identifies future unseen problems before they occur. The insight provided in the report exhibits what is actually going on in your portfolio. This likely includes adverse selection, impact of price changes with unintended consequences, and the emerging trends in the composition of the book. The analysis results not only reveal past trends, but also predict future impact.</p>

</div>
</body>
</html>
```